Business Card Design for Orthopaedic Surgeon

This is a double-sided glossy business card. I prefer baby blue, teal, and green as color schemes. I have my logo already (many colors that you can choose from). I have photos and examples of my old card (very bland but has the information in it). I also have one that my assistant tried to design, but the writing is too small and I don't love the formatting. But it is close!
I would like my logo to be on the business card but I'm uploading my logo in many different colors so you can choose which one looks best based on the color scheme. I also uploaded many sized headshots so you can choose the best resolution one.

Additional information:
Correct business address:
4382 NW 58th Lane, Suite 305
Tamarac, FL 33417

Everything else on both business cards are accurate.

I actually need 2 different business cards generated. One that includes my cell phone number-- Personal cell: 585-314-9062 in addition to Office phone: (954) 316-4870 and Office Fax: 954-316-4881. Again, one card would have my personal cell and one wouldn't

Overall I just think the baby blue card (uploaded) is missing something on the front--of course it is also missing my office phone/fax/personal cell. I do want my website on the front too. Email: info@wellsorthocare.example

You can use your discretion about what goes on the front vs. what goes on the back to eliminated clutter.

Oh and on the back, I would like to list "Conditions Treated" (not specialties include). The list is:
Carpal Tunnel
Trigger Finger
Ganglion Cysts
Hand Tumors
Han & Wrist Arthritis
Hand, Wrist & Elbow Tendonitis
Fractures of the Hand, Wrist, Elbow and Humerus
Nerve Injuries of the Hand, Wrist & Elbow
Microsurgery
Wrist Arthroscopy
Endoscopic Surgery

Target Market(s)

Primary care doctors, Lawyers, patients

Industry/Entity Type

Medical

Contact Information for Business Card

Please see above in project description

Colors

Designer to choose colors to be used in the design.

Requirements
Must have
• -Correct office info, Board Certified Orthopaedic Hand & Upper Extremity Surgeon
Nice to have
• Something that is classy and wow!

```html
<!DOCTYPE html>
<html lang="en">
<head>
<meta charset="utf-8">
<title>Renata Wells, M.D – Business Card</title>
<link rel="stylesheet" href="https://fonts.googleapis.com/css2?family=Montserrat:wght@400;500;700&display=swap">
<style>
  :root {
    --backdrop: #4a4a4a;
    --card: #121212;
    --edge: #ffffff;
    --ink: #ffffff;
    --ink-soft: #e6e6e6;
    --photo-light: #f2f2f2;
    --photo-dark: #8a8a8a;
  }
  * { box-sizing: border-box; margin: 0; padding: 0; }
  html, body {
    width: 1200px; height: 801px; overflow: hidden;
    background: var(--backdrop);
    font-family: "Montserrat", sans-serif;
    color: var(--ink);
  }
  .sheet {
    width: 1200px; height: 801px;
    display: flex; align-items: center; justify-content: center; gap: 32px;
  }
  .card {
    position: relative;
    width: 560px; height: 320px;
    background: var(--card);
    border: 3px solid var(--edge);
    border-radius: 18px;
    overflow: hidden;
  }

  /* Front */
  .front-photo {
    position: absolute; left: 30px; top: 28px;
    width: 150px; height: 138px;
    border: 2px solid var(--edge);
    background: radial-gradient(circle at 30% 30%, var(--photo-light), var(--photo-dark));
  }
  .doctor-name {
    position: absolute; left: 30px; top: 188px;
    font-weight: 700; font-size: 21px; letter-spacing: 0.5px;
  }
  .doctor-title {
    position: absolute; left: 44px; top: 222px;
    font-size: 14px; line-height: 22px; color: var(--ink-soft);
  }
  .brand {
    position: absolute;
    display: flex; align-items: center; gap: 10px;
  }
  .brand-dot {
    border: 3px solid var(--ink); border-radius: 50%;
  }
  .brand-name {
    font-weight: 700; font-size: 17px; letter-spacing: 3px;
  }
  .front-brand { left: 320px; top: 34px; }
  .front-brand .brand-dot { width: 56px; height: 56px; }

  .contact-list {
    position: absolute; left: 300px; top: 120px;
    list-style: none; font-size: 12.5px; line-height: 18px;
  }
  .contact-list li { display: flex; align-items: flex-start; gap: 9px; margin-bottom: 3px; }
  .contact-list svg { flex: none; width: 13px; height: 13px; margin-top: 2px; fill: var(--ink); }

  /* Back */
  .back-brand { right: 32px; top: 44px; }
  .back-brand .brand-dot { width: 70px; height: 70px; }
  .conditions {
    position: absolute; left: 34px; top: 78px;
    list-style: none; font-size: 13.5px; line-height: 19.5px;
  }
  .conditions li::before {
    content: ""; display: inline-block;
    width: 6px; height: 6px; border-radius: 50%;
    background: var(--ink); margin-right: 7px; vertical-align: middle;
  }
</style>
</head>
<body>
<main class="sheet">

  <section class="card card-front">
    <div class="front-photo" role="img" aria-label="Headshot portrait of the surgeon"></div>
    <h1 class="doctor-name">RENATA WELLS, M.D</h1>
    <p class="doctor-title">Board Certified<br>Orthopaedic Hand &amp; Upper<br>Extremity Surgeon</p>

    <div class="brand front-brand">
      <span class="brand-dot"></span>
      <span class="brand-name">WELLS HAND</span>
    </div>

    <ul class="contact-list">
      <li>
        <svg viewBox="0 0 24 24"><path d="M12 2a7 7 0 0 0-7 7c0 5 7 13 7 13s7-8 7-13a7 7 0 0 0-7-7zm0 9.5A2.5 2.5 0 1 1 12 6.5a2.5 2.5 0 0 1 0 5z"/></svg>
        <span>4382 NW 58th Lane,<br>Suite 305 Tamarac, FL 33417</span>
      </li>
      <li>
        <svg viewBox="0 0 24 24"><path d="M6.6 10.8a15 15 0 0 0 6.6 6.6l2.2-2.2a1 1 0 0 1 1-.25 11.4 11.4 0 0 0 3.6.57 1 1 0 0 1 1 1V20a1 1 0 0 1-1 1A17 17 0 0 1 3 4a1 1 0 0 1 1-1h3.5a1 1 0 0 1 1 1c0 1.25.2 2.45.57 3.57a1 1 0 0 1-.25 1z"/></svg>
        <span>(954) 316-4870</span>
      </li>
      <li>
        <svg viewBox="0 0 24 24"><path d="M6 2h10v6H6zM4 9h16a2 2 0 0 1 2 2v7h-4v4H6v-4H2v-7a2 2 0 0 1 2-2zm4 8v3h8v-3z"/></svg>
        <span>954-316-4881</span>
      </li>
      <li>
        <svg viewBox="0 0 24 24"><path d="M2 5h20v14H2zm2 2v.5l8 5 8-5V7z"/></svg>
        <span>info@wellsorthocare.example</span>
      </li>
      <li>
        <svg viewBox="0 0 24 24"><path d="M12 2a10 10 0 1 0 0 20 10 10 0 0 0 0-20zm6.9 9h-3a15 15 0 0 0-1.3-5.6A8 8 0 0 1 18.9 11zM12 4.1c1 1.3 1.8 3.9 1.9 6.9h-3.8c.1-3 .9-5.6 1.9-6.9zM9.4 5.4A15 15 0 0 0 8.1 11h-3a8 8 0 0 1 4.3-5.6zM5.1 13h3a15 15 0 0 0 1.3 5.6A8 8 0 0 1 5.1 13zm6.9 6.9c-1-1.3-1.8-3.9-1.9-6.9h3.8c-.1 3-.9 5.6-1.9 6.9zm2.6-1.3a15 15 0 0 0 1.3-5.6h3a8 8 0 0 1-4.3 5.6z"/></svg>
        <span>www.wellsorthocare.example</span>
      </li>
    </ul>
  </section>

  <section class="card card-back">
    <div class="brand back-brand">
      <span class="brand-dot"></span>
      <span class="brand-name">WELLS HAND</span>
    </div>
    <ul class="conditions">
      <li>Carpal Tunnel</li>
      <li>Trigger Finger</li>
      <li>Ganglion Cysts</li>
      <li>Hand Tumors</li>
      <li>Han &amp; Wrist Arthritis</li>
      <li>Hand, Wrist &amp; Elbow Tendonitis</li>
      <li>Fractures of the Hand, Wrist, Elbow and Humerus</li>
      <li>Nerve Injuries of the Hand, Wrist &amp; Elbow</li>
      <li>Microsurgery</li>
      <li>Wrist Arthroscopy</li>
      <li>Endoscopic Surgery</li>
    </ul>
  </section>

</main>
</body>
</html>
```